Business Card for Willowcrest Terrain Advisors

We need a business card for Willowcrest Terrain Advisors. The company website address is provided below. The company logo is attached. We provide specialized permafrost services to the mining, transportation, and oil & gas industries. The card should be prepared for:
Dominic Halloway, PhD.
Willowcrest Terrain Advisors
PO Box 418529
Birch Hollow, Alaska 99612
Direct: +1-907-555-2964
Email: dhalloway@terrainadvisors-example.com
Website: www.willowcrestterrainadvisors-example.com

```html
<!DOCTYPE html>
<html lang="en">
<head>
<meta charset="utf-8">
<title>Willowcrest Terrain Advisors – Business Card</title>
<link href="https://fonts.googleapis.com/css2?family=Montserrat:wght@400;700&display=swap" rel="stylesheet">
<style>
  :root {
    --navy: #121a24;
    --paper: #ffffff;
    --ink: #141c26;
    --backdrop: #e9e6e1;
    --muted-light: #d9dde2;
  }
  * { box-sizing: border-box; margin: 0; padding: 0; }
  html, body { width: 1200px; height: 931px; overflow: hidden; }
  body {
    background: var(--backdrop);
    font-family: "Montserrat", sans-serif;
    position: relative;
  }
  .card {
    position: absolute;
    width: 620px;
    height: 354px;
    border-radius: 22px;
    box-shadow: 0 10px 28px rgba(0,0,0,.18);
    overflow: hidden;
  }
  .card-back {
    left: 60px; top: 80px;
    background: var(--navy);
    display: flex; align-items: center; justify-content: center;
  }
  .card-front {
    left: 520px; top: 490px;
    background: var(--paper);
    color: var(--ink);
  }
  .wordmark {
    font-weight: 700;
    text-transform: uppercase;
    letter-spacing: .08em;
    line-height: 1.15;
    text-align: center;
  }
  .card-back .wordmark { color: var(--paper); font-size: 34px; }
  .card-front .wordmark {
    position: absolute; right: 34px; top: 36px;
    font-size: 22px; color: var(--ink);
  }
  .divider-long {
    position: absolute; left: 150px; right: 30px; top: 152px;
    height: 2px; background: var(--ink);
  }
  .person { position: absolute; left: 34px; top: 172px; }
  .person-name { font-weight: 700; font-size: 22px; }
  .person-role { font-size: 14px; margin-top: 2px; }
  .divider-short { width: 230px; height: 2px; background: var(--ink); margin: 10px 0 12px; }
  .contact-list { list-style: none; font-size: 12.5px; }
  .contact-list li { display: flex; align-items: center; gap: 10px; margin-bottom: 7px; }
  .contact-list svg { width: 14px; height: 14px; flex: none; }
  .address {
    position: absolute; right: 34px; top: 180px;
    font-size: 13px; line-height: 1.4; text-align: left;
  }
</style>
</head>
<body>

<section class="card card-back" aria-label="Card back">
  <div class="wordmark">Willowcrest<br>Terrain Advisors</div>
</section>

<section class="card card-front" aria-label="Card front">
  <div class="wordmark">Willowcrest<br>Terrain Advisors</div>
  <div class="divider-long"></div>

  <div class="person">
    <div class="person-name">Dominic Halloway, PhD.</div>
    <div class="person-role">Managing Director</div>
    <div class="divider-short"></div>
    <ul class="contact-list">
      <li>
        <svg viewBox="0 0 16 16" aria-hidden="true"><path fill="#141c26" d="M3.6 1.5l2.3 2.6-1.3 1.7c.9 2 2.5 3.6 4.5 4.5l1.7-1.3 2.6 2.3-1.4 2.5C6.6 13.6 2.4 9.4 1.2 3.9z"/></svg>
        +1-907-555-2964
      </li>
      <li>
        <svg viewBox="0 0 16 16" aria-hidden="true"><rect x="1" y="3" width="14" height="10" fill="#141c26"/><path d="M1 3l7 5 7-5" fill="none" stroke="#fff" stroke-width="1.2"/></svg>
        dhalloway@terrainadvisors-example.com
      </li>
      <li>
        <svg viewBox="0 0 16 16" aria-hidden="true"><circle cx="8" cy="8" r="7" fill="#141c26"/><path d="M1 8h14M8 1c-3 3-3 11 0 14M8 1c3 3 3 11 0 14" fill="none" stroke="#fff" stroke-width="1"/></svg>
        www.willowcrestterrainadvisors-example.com
      </li>
    </ul>
  </div>

  <div class="address">PO Box 418529<br>Birch Hollow, Alaska 99612</div>
</section>

</body>
</html>
```